I need to redesign this website. Modern Fun Professional Redesign For www.JollyPerkHub.com = New Name www.ClaimVouchly.com

Use existing content as it is on website exactly and we will revise after initial mock ups.

The new name will be ClaimVouchly.com please make a quick logo for this site too while redesigning.

Make it look like an official website....

Target Market(s)

Consumers that are redeeming certificates that businesses gave to them as a gift for customer loyalty,e tc.

Industry/Entity Type

It Professional

Logo Text

www.ClaimVouchly.com

Number of Pages Required

4 page

Colors

Designer to choose colors to be used in the design.

Requirements
Must have
• Must look professional, build trust and credibility.
Nice to have
• open
Should not have
• open

```html
<!DOCTYPE html>
<html lang="en">
<head>
<meta charset="utf-8">
<title>ClaimVouchly – Redeem Processing Center</title>
<link rel="stylesheet" href="https://fonts.googleapis.com/css2?family=Jost:ital,wght@0,400;0,500;0,700;1,400&family=Anton&display=swap">
<style>
:root{
  --gold:#d3a238;
  --gold-dark:#b8862a;
  --teal:#5bbfc9;
  --teal-light:#cdebee;
  --white:#ffffff;
  --ink:#444444;
  --muted:#6a6a6a;
  --orange:#e8762a;
  --black:#0d0d0d;
  --field:#eeeeee;
}
*{margin:0;padding:0;box-sizing:border-box}
html,body{width:1200px;height:3025px;overflow:hidden}
body{font-family:"Jost",sans-serif;color:var(--ink);background:var(--white);position:relative}
.abs{position:absolute}

/* header */
.site-header{position:absolute;left:0;top:0;width:1200px;height:84px;background:var(--gold);z-index:3}
.nav-link{position:absolute;top:22px;height:46px;line-height:46px;color:var(--white);font-size:17px;font-weight:500;text-transform:uppercase;text-decoration:none;padding:0 22px}
.nav-link.active{background:var(--teal);border-radius:4px}
.brand-badge{position:absolute;left:465px;top:-72px;width:270px;height:270px;border-radius:50%;background:var(--white);z-index:4;text-align:center}
.brand-name{position:absolute;left:0;right:0;top:145px;font-size:36px;font-weight:700;color:var(--orange);letter-spacing:-.5px}
.brand-tag{position:absolute;left:0;right:0;top:194px;font-size:13px;color:var(--muted)}

/* hero */
.hero{position:absolute;left:0;top:84px;width:1200px;height:592px;
  background:linear-gradient(160deg,#1a1524 0%,#3b2a35 35%,#5a3a2a 60%,#20161c 100%)}
.hero-title{position:absolute;left:0;right:0;top:284px;text-align:center;font-family:"Anton",sans-serif;font-size:50px;line-height:62px;color:var(--white);letter-spacing:1.5px;text-shadow:2px 3px 4px rgba(0,0,0,.6)}
.slider-arrow{position:absolute;width:24px;height:60px}

/* welcome */
.welcome{position:absolute;left:0;top:676px;width:1200px;height:314px;background:var(--gold);text-align:center;color:var(--white)}
.section-title{font-family:"Jost",sans-serif;font-weight:700;text-transform:uppercase;font-size:38px;letter-spacing:.5px}
.welcome .section-title{position:absolute;left:0;right:0;top:56px}
.welcome-copy{position:absolute;left:170px;width:860px;top:120px;font-size:13px;line-height:24px}
.welcome-copy p+p{margin-top:8px}
.btn{display:block;background:var(--teal);color:var(--white);font-weight:700;text-transform:uppercase;text-align:center;border-radius:4px}
.read-more{position:absolute;left:503px;top:960px;width:194px;height:58px;line-height:58px;font-size:20px;z-index:2}

/* certificate */
.certificate{position:absolute;left:0;top:990px;width:1200px;height:512px}
.cert-title{position:absolute;left:78px;top:88px;color:var(--gold);font-size:38px}
.cert-lead{position:absolute;left:78px;top:144px;width:540px;font-style:italic;font-size:16px;line-height:30px;color:var(--muted)}
.cert-form{position:absolute;left:78px;top:232px;width:518px;height:58px;background:var(--field);border-radius:4px}
.cert-form span{position:absolute;left:24px;top:19px;font-size:14px;font-style:italic;color:var(--muted)}
.go-btn{position:absolute;right:4px;top:4px;width:50px;height:50px;line-height:50px;font-size:20px}
.cert-copy{position:absolute;left:78px;top:326px;width:560px;font-size:14px;line-height:27px;color:var(--muted)}
.cert-copy p+p{margin-top:22px}
.photo-frame{position:absolute;left:670px;top:80px;width:453px;height:375px;background:var(--white);padding:10px;box-shadow:0 4px 14px rgba(0,0,0,.3)}
.photo-fill{width:100%;height:100%;background:linear-gradient(135deg,#2d3f55 0%,#6f8aa3 45%,#c6cfd8 75%,#8a96a2 100%)}

/* testimonials */
.testimonials{position:absolute;left:0;top:1502px;width:1200px;height:530px;
  background:linear-gradient(120deg,#c99a3b 0%,#d7ad55 40%,#c38f33 70%,#b98a37 100%)}
.testimonials .section-title{position:absolute;left:0;right:0;top:62px;text-align:center;color:var(--white)}
.quote{position:absolute;top:144px;width:335px;background:var(--teal-light);border-radius:3px;padding:22px 24px;text-align:center;font-size:14px;line-height:26px;color:var(--ink)}
.quote::after{content:"";position:absolute;bottom:-24px;border-style:solid;border-width:24px 24px 0 0;border-color:var(--teal-light) transparent transparent transparent}
.quote.left{left:76px;height:160px}
.quote.left::after,.quote.right::after{left:140px}
.quote.center{left:435px;height:224px;width:333px;background:var(--teal);color:var(--white)}
.quote.center::after{left:140px;border-color:var(--teal) transparent transparent transparent}
.quote.right{left:790px;width:332px;height:160px}
.client{position:absolute;color:var(--white)}
.avatar{position:absolute;width:62px;height:62px;border-radius:50%;border:3px solid var(--white);background:linear-gradient(135deg,#6b4a3a,#c89a7a)}
.client-name{position:absolute;left:78px;top:4px;font-weight:700;font-size:17px;text-transform:uppercase;white-space:nowrap}
.client-place{position:absolute;left:78px;top:30px;font-size:14px;white-space:nowrap}

/* contact */
.contact{position:absolute;left:0;top:2032px;width:1200px;height:648px;
  background:linear-gradient(180deg,#f3f5f7 0%,#dfe5ea 40%,#b9c4cd 70%,#9aa7b1 100%)}
.agent-photo{position:absolute;left:150px;top:60px;width:320px;height:588px;border-radius:160px 160px 0 0;background:linear-gradient(180deg,#8a6a52 0%,#5c6a78 55%,#7b8893 100%)}
.contact-box{position:absolute;left:555px;top:46px;width:525px;height:602px;background:var(--gold);box-shadow:0 4px 14px rgba(0,0,0,.35);text-align:center;color:var(--white)}
.contact-box .section-title{position:absolute;left:0;right:0;top:58px;font-size:40px}
.contact-lead{position:absolute;left:40px;right:40px;top:118px;font-size:15px;font-style:italic;line-height:26px}
.field{position:absolute;left:42px;width:433px;height:46px;background:var(--white);text-align:left;padding:14px 14px;font-size:13px;color:var(--muted)}
.field.message{height:94px}
.submit{position:absolute;left:173px;top:452px;width:167px;height:56px;line-height:56px;font-size:20px}

/* footer */
.site-footer{position:absolute;left:0;top:2680px;width:1200px;height:345px;background:var(--black);text-align:center;color:#bbbbbb}
.footer-brand{position:absolute;left:0;right:0;top:82px;font-size:34px;font-weight:700;color:var(--orange)}
.footer-tag{position:absolute;left:0;right:0;top:130px;font-size:13px;color:#999}
.social{position:absolute;top:178px;width:48px;height:48px;border-radius:50%;border:2px solid var(--gold)}
.social.solid{background:var(--gold)}
.address{position:absolute;left:0;right:0;top:250px;font-size:14px}
.copyright{position:absolute;left:0;right:0;top:277px;font-size:14px}
</style>
</head>
<body>

<header class="site-header">
  <a class="nav-link active" style="left:190px">Home</a>
  <a class="nav-link" style="left:305px">Contact Us</a>
  <a class="nav-link" style="left:748px">Testimonials</a>
  <a class="nav-link" style="left:910px">Terms</a>
</header>
<div class="brand-badge">
  <div class="brand-name">ClaimVouchly</div>
  <div class="brand-tag">Redeem Processing Center</div>
</div>

<section class="hero" role="img" aria-label="Night city skyline with illuminated towers and light trails">
  <h1 class="hero-title">What Good Is It To Receive A Gift<br>Certificate If You Can't Use It?</h1>
  <svg class="slider-arrow" style="left:28px;top:284px" viewBox="0 0 24 60"><polyline points="20,4 4,30 20,56" fill="none" stroke="#fff" stroke-width="2"/></svg>
  <svg class="slider-arrow" style="left:1148px;top:284px" viewBox="0 0 24 60"><polyline points="4,4 20,30 4,56" fill="none" stroke="#fff" stroke-width="2"/></svg>
</section>

<section class="welcome">
  <h2 class="section-title">Welcome to ClaimVouchly</h2>
  <div class="welcome-copy">
    <p>Lorem Ipsum is simply dummy text of the printing and typesetting industry. Lorem Ipsum has been the industry's standard dummy text ever since the 1500s, when an unknown printer took a galley of type and scrambled it to make a type specimen book. It has survived not only five centuries, but also the leap into electronic typesetting.</p>
    <p>Lorem Ipsum is simply dummy text of the printing and typesetting industry. Lorem Ipsum has been the industry's standard dummy text ever since the 1500s, when an unknown printer took a galley of type and scrambled.</p>
  </div>
</section>
<a class="btn read-more">Read More</a>

<section class="certificate">
  <h2 class="section-title cert-title">Get Your Certificate</h2>
  <p class="cert-lead">Please Enter a Valid Certificate Id In The Form Below To redeem Your Certificate And To View Faq's,Terms and Locations.</p>
  <div class="cert-form"><span>Enter Eamil Id *</span><a class="btn go-btn">Go</a></div>
  <div class="cert-copy">
    <p>JollyPerkHub.com is a leading company in travel certificate fulfillment.</p>
    <p>Our goal is to make it easy for you to redeem your certificate and our philosophy is this: "What good is it to receive a gift certificate if you can't use it?</p>
  </div>
  <div class="photo-frame"><div class="photo-fill" role="img" aria-label="Traveller on the phone in an airport terminal in front of a departures board"></div></div>
</section>

<section class="testimonials" role="img" aria-label="Warm golden-tinted photo of friends outdoors behind the testimonials">
  <h2 class="section-title">Waht Oue Client Say About Us</h2>
  <svg class="slider-arrow" style="left:24px;top:216px" viewBox="0 0 24 60"><polyline points="20,4 4,30 20,56" fill="none" stroke="#fff" stroke-width="2"/></svg>
  <svg class="slider-arrow" style="left:1152px;top:216px" viewBox="0 0 24 60"><polyline points="4,4 20,30 4,56" fill="none" stroke="#fff" stroke-width="2"/></svg>

  <div class="quote left">" Hi! This is a picture of my darling taken in Falls Church last weekend! We had a great time. Thank you! "</div>
  <div class="quote center">" My vacation was excellent! We started in Milano, and visited the Duomo Cathedral; then we went to Lako Como, and then proceeded to Sorrento; Amalfi; Positano; Bari and ended in the Abbruzzi area. Wonderful people, weather, great food and great wine! "</div>
  <div class="quote right">" My Las Vegas tour was excellent &amp; memorable. I really enjoyed it. Thank you for your help! "</div>

  <div class="client" style="left:100px;top:338px"><div class="avatar" role="img" aria-label="Client portrait"></div><div class="client-name">Marcus T.</div><div class="client-place">Geyserville, CA</div></div>
  <div class="client" style="left:455px;top:400px"><div class="avatar" role="img" aria-label="Client portrait"></div><div class="client-name">Lena R.</div><div class="client-place">Port Orange, FL</div></div>
  <div class="client" style="left:812px;top:338px"><div class="avatar" role="img" aria-label="Client portrait"></div><div class="client-name">Ravi K.</div><div class="client-place">Jamaica, NY</div></div>
</section>

<section class="contact" role="img" aria-label="Snowy mountain landscape background">
  <div class="agent-photo" role="img" aria-label="Smiling support agent wearing a headset"></div>
  <div class="contact-box">
    <h2 class="section-title">Contact Us</h2>
    <p class="contact-lead">If you have any questions about how to redeem a certain certificate, please contact us. We are here to help.</p>
    <div class="field" style="top:188px">Name*</div>
    <div class="field" style="top:243px">Eamil*</div>
    <div class="field" style="top:298px">Certificate ID #*</div>
    <div class="field message" style="top:353px">How May We Assist You?*</div>
    <a class="btn submit">Submit</a>
  </div>
</section>

<footer class="site-footer">
  <div class="footer-brand">ClaimVouchly</div>
  <div class="footer-tag">Redeem Processing Center</div>
  <span class="social solid" style="left:520px" aria-label="Social link"></span>
  <span class="social" style="left:576px" aria-label="Social link"></span>
  <span class="social" style="left:632px" aria-label="Social link"></span>
  <p class="address">4120 Linden Park Ave Ste B #210 Fairvale, Ca 90417</p>
  <p class="copyright">©ClaimVouchly - 2017 All Rights Reserved</p>
</footer>

</body>
</html>
```